Business Report Cover

We need a revamped quarterly report cover to send to our clients. We asset manage commercial and residential properties throughout the the United States. We use a .pdf version of a cover that we've used for years but would like a fresh updated look for 2018. The cover should include our company logo (KVL Holdings) and a photo of the property as well as the Quarter/Year of the report.

Industry/Entity Type

Business

```html
<!DOCTYPE html>
<html lang="en">
<head>
<meta charset="utf-8">
<title>KVL Holdings – Quarterly Operating Report Q1 2018</title>
<link href="https://fonts.googleapis.com/css2?family=Montserrat:wght@400;600;700;800&display=swap" rel="stylesheet">
<style>
  :root{
    --backdrop:#e6e6e6;
    --paper:#ffffff;
    --ink:#1d1f24;
    --green:#2f9a5e;
    --green-deep:#1f7a45;
    --navy:#34405a;
    --slate:#3a4150;
    --mist:#d9dbdf;
    --white:#ffffff;
  }
  *{box-sizing:border-box;margin:0;padding:0}
  html,body{width:1200px;height:870px;overflow:hidden;background:var(--backdrop)}
  body{font-family:"Montserrat",Arial,sans-serif;color:var(--ink);position:relative}
  .report-cover{
    position:absolute;left:315px;top:25px;width:570px;height:820px;
    background:var(--paper);overflow:hidden;
  }
  .cover-art{position:absolute;inset:0;width:100%;height:100%}
  .report-heading{position:absolute;left:43px;top:38px;line-height:1.25}
  .report-title{font-weight:700;font-size:17px}
  .report-quarter{font-weight:400;font-size:17px}
  .report-year{font-weight:800;font-size:30px;color:var(--green);margin-top:4px;line-height:1}
  .brand-name{
    position:absolute;right:49px;top:40px;
    font-weight:800;font-size:24px;color:var(--ink);letter-spacing:.5px;
    display:flex;align-items:center;gap:8px;
  }
  .brand-mark{width:12px;height:12px;background:var(--green)}
  .property{position:absolute;left:40px;top:732px;color:var(--white)}
  .property-name{font-weight:700;font-size:16px;margin-bottom:4px}
  .property-address{font-weight:400;font-size:10.5px;line-height:1.5}
</style>
</head>
<body>
  <main class="report-cover">
    <svg class="cover-art" viewBox="0 0 358 515" preserveAspectRatio="none" aria-hidden="false">
      <defs>
        <linearGradient id="photoTone" x1="0" y1="0" x2="0" y2="1">
          <stop offset="0" stop-color="#6f7580"/>
          <stop offset=".55" stop-color="#4a515d"/>
          <stop offset="1" stop-color="#2f3542"/>
        </linearGradient>
        <linearGradient id="footShade" x1="0" y1="0" x2="0" y2="1">
          <stop offset="0" stop-color="#2b3140" stop-opacity="0"/>
          <stop offset="1" stop-color="#2b3140" stop-opacity=".9"/>
        </linearGradient>
      </defs>
      <g role="img" aria-label="Photo of the Alder Grove Market convenience store and fuel canopy with shrubs and a bare tree">
        <polygon points="0,265 127,190 186,150 250,200 358,200 358,345 300,405 358,460 358,515 0,515" fill="url(#photoTone)"/>
      </g>
      <polygon points="0,265 250,205 250,395 120,395" fill="var(--green)" opacity=".72"/>
      <polygon points="60,250 160,230 250,300 140,340" fill="var(--green-deep)" opacity=".5"/>
      <polygon points="186,150 272,206 186,222" fill="var(--mist)" opacity=".85"/>
      <polygon points="127,188 186,150 186,222" fill="var(--navy)"/>
      <polygon points="22,193 43,182 43,205" fill="var(--green)"/>
      <polygon points="52,174 85,192 52,210" fill="var(--navy)"/>
      <polygon points="300,405 358,345 358,460" fill="var(--paper)"/>
      <rect x="0" y="410" width="358" height="105" fill="url(#footShade)"/>
      <polygon points="253,497 308,470 308,515 253,515" fill="var(--green)" opacity=".85"/>
    </svg>

    <header class="report-heading">
      <h1 class="report-title">Quarterly Operating Report</h1>
      <p class="report-quarter">1st Quarter</p>
      <p class="report-year">2018</p>
    </header>

    <div class="brand-name"><span class="brand-mark"></span>KVL Holdings</div>

    <section class="property">
      <h2 class="property-name">Alder Grove Market</h2>
      <p class="property-address">4120 NE Alder Grove Rd.<br>Ridgefield, WA 98642</p>
    </section>
  </main>
</body>
</html>
```